Re Design of Business Cards

We a Technology & Telecommunications company, we supply computer repairs suppy and services to home and business's, we also a Telecommunications company as well and that we supply Internet, Mobile Voice and Data and Voice Lines to home and business as well we want to get our business cards re designed that stand out but also state what we can do and that we also come to you, there is 4 of us in the business so we all need same business card design but just different names and phone numbers on all.
Ive upload our Logo as well. and current looking business cards.

Our current business cards does not make me excited and or stand out, to dark and does not say what we do, we leave our business cards in letter boxes some times and in receptions of villages for retiress so the reception can hand out, few times now there asked what do you do, so thinking one side is our contact details and other is our services

I think I like to also put our address onto it as well, very simple as its also my home address but it be good to have it on there

48 Pellow St - Bateau Bay NSW 2261

We should also have our business rego number which is a ABN

ABN: 37 904 516 283

this way we all covered and we look very Professional

We would like to make some Points, 1st of All we just found out we do not need out ABN on our Business Cards so we can Remove that please

we would like the address for the business to be on cards as well,

On the flip side of the Business Cards we would like to list some of our services as below

High-Speed Internet for Home & Business
Managed IT Services & Support
Network Setup & Optimization
VoIP & Mobile Voice Solutions
Wi-Fi Installation & Troubleshooting
Smart Home & Office Technology
Data Backup & Cybersecurity
Onsite Home and Or Business

```html
<!DOCTYPE html>
<html lang="en">
<head>
<meta charset="utf-8">
<title>Tornlink Business Card</title>
<link href="https://fonts.googleapis.com/css2?family=Montserrat:wght@400;500;600;700&display=swap" rel="stylesheet">
<style>
  :root {
    --stage: #1b1c1c;
    --paper: #f3f3f3;
    --paper-shade: #e9e9e9;
    --ink: #2b2b2b;
    --orange: #e2612a;
    --orange-deep: #c9511f;
    --green: #2f9e3c;
    --teal: #17403f;
    --teal-soft: #1d4a48;
    --white: #ffffff;
  }
  * { box-sizing: border-box; margin: 0; padding: 0; }
  html, body { width: 1200px; height: 1059px; overflow: hidden; }
  body {
    background: var(--stage);
    font-family: "Montserrat", Arial, sans-serif;
    position: relative;
  }
  .card {
    position: absolute;
    left: 257px;
    width: 687px;
    height: 391px;
    border-radius: 18px;
    overflow: hidden;
  }
  .card-front { top: 89px; background: var(--paper); color: var(--ink); }
  .card-back { top: 547px; background: var(--teal); color: var(--white); }

  .front-shade {
    position: absolute; left: 380px; top: 180px;
    width: 282px; height: 282px; border-radius: 50%;
    background: radial-gradient(circle, var(--paper-shade) 0%, var(--paper-shade) 45%, rgba(233,233,233,0) 72%);
  }

  .name-band {
    position: absolute;
    left: 0; top: 60px;
    width: 390px; height: 60px;
    background: linear-gradient(90deg, var(--orange-deep), var(--orange));
    color: var(--white);
    padding: 8px 0 0 40px;
  }
  .person-name { font-weight: 700; font-size: 23px; letter-spacing: .4px; line-height: 25px; }
  .person-role { font-weight: 400; font-size: 17px; line-height: 22px; }

  .brand { position: absolute; display: flex; align-items: center; }
  .brand-mark { background: var(--orange); flex: none; }
  .brand-text { display: flex; flex-direction: column; }
  .brand-name { font-weight: 600; color: var(--orange); line-height: 1; }
  .brand-tagline { font-weight: 500; text-transform: uppercase; letter-spacing: .6px; margin-top: 5px; }

  .card-front .brand { left: 410px; top: 66px; }
  .card-front .brand-mark { width: 18px; height: 18px; margin-right: 14px; }
  .card-front .brand-name { font-size: 28px; }
  .card-front .brand-tagline { font-size: 8px; color: var(--ink); }

  .address {
    position: absolute; left: 40px; top: 191px;
    font-size: 16.5px; line-height: 21px;
  }
  .contacts { position: absolute; left: 40px; top: 344px; list-style: none; transform: translateY(-100%); }
  .contacts { top: 256px; transform: none; }
  .contacts li {
    display: flex; align-items: center;
    font-size: 16.5px; height: 25px;
  }
  .contacts svg { width: 14px; height: 14px; margin-right: 7px; fill: var(--green); }

  .back-glow {
    position: absolute; left: 200px; top: 55px;
    width: 460px; height: 460px; border-radius: 50%;
    background: var(--teal-soft); opacity: .55;
  }
  .card-back .brand { left: 172px; top: 86px; }
  .card-back .brand-mark { width: 26px; height: 26px; margin-right: 20px; }
  .card-back .brand-name { font-size: 42px; }
  .card-back .brand-tagline { font-size: 9.5px; color: var(--white); }

  .services-heading {
    position: absolute; left: 32px; right: 32px; top: 216px;
    display: flex; align-items: center; gap: 12px;
  }
  .services-heading::before, .services-heading::after {
    content: ""; flex: 1; height: 1px; background: var(--green);
  }
  .services-heading h2 {
    font-size: 23px; font-weight: 700; color: var(--orange); letter-spacing: .5px;
  }
  .services {
    position: absolute; left: 0; right: 0; top: 255px;
    text-align: center; font-size: 16.6px; line-height: 26.6px;
  }
  .services .sep { color: var(--orange); margin: 0 6px; }
</style>
</head>
<body>

<section class="card card-front">
  <div class="front-shade" role="img" aria-label="Faint soft brand shape in the corner"></div>
  <div class="name-band">
    <div class="person-name">REECE CALLOWAY</div>
    <div class="person-role">Sales Consultant</div>
  </div>
  <div class="brand">
    <span class="brand-mark"></span>
    <div class="brand-text">
      <span class="brand-name">Tornlink</span>
      <span class="brand-tagline">Technology &amp; Telecommunications</span>
    </div>
  </div>
  <p class="address">48 Pellow St - Bateau<br>Bay NSW 2261</p>
  <ul class="contacts">
    <li><svg viewBox="0 0 16 16"><path d="M3.5 1.5l2.5 3-1.6 1.6c.8 2 2.5 3.7 4.5 4.5L10.5 9l3 2.5-1.5 2.5C6.5 14 2 9.5 1.5 3.5z"/></svg>1800 614 372</li>
    <li><svg viewBox="0 0 16 16"><path d="M4.5 1h7a1 1 0 0 1 1 1v12a1 1 0 0 1-1 1h-7a1 1 0 0 1-1-1V2a1 1 0 0 1 1-1zm.5 2v9h6V3zm3 9.7a.8.8 0 1 0 0 1.6.8.8 0 0 0 0-1.6z"/></svg>0412 958 306</li>
    <li><svg viewBox="0 0 16 16"><path d="M1 4h14v9H1zm1.5 1.2v.3L8 9l5.5-3.5v-.3z"/></svg>reece@tornlink.com.au</li>
    <li><svg viewBox="0 0 16 16"><circle cx="8" cy="8" r="7"/><path d="M1 8h14M8 1c3 3 3 11 0 14M8 1c-3 3-3 11 0 14" stroke="#f3f3f3" stroke-width="1" fill="none"/></svg>www.tornlink.com.au</li>
  </ul>
</section>

<section class="card card-back">
  <div class="back-glow"></div>
  <div class="brand">
    <span class="brand-mark"></span>
    <div class="brand-text">
      <span class="brand-name">Tornlink</span>
      <span class="brand-tagline">Technology &amp; Telecommunications</span>
    </div>
  </div>
  <div class="services-heading"><h2>OUR SERVICES</h2></div>
  <p class="services">
    High-Speed Internet for Home &amp; Business<span class="sep">•</span>Managed IT Services &amp; Support<br>
    Network Setup &amp; Optimization<span class="sep">•</span>VoIP &amp; Mobile Voice Solutions<br>
    Wi-Fi Installation &amp; Troubleshooting<span class="sep">•</span>Smart Home &amp; Office Technology<br>
    Data Backup &amp; Cybersecurity<span class="sep">•</span>Onsite Home and Or Business
  </p>
</section>

</body>
</html>
```